KRV

I just wrote a novel that I plan on marketing through my website. Please use my uploaded files to add on to your design... The name of the book is "Ashes beneath the orchard".

Industry/Entity Type

Marketing

Font styles to use
Serif
Sans Serif

Colors

Designer to choose colors to be used in the design.

```html
<!DOCTYPE html>
<html lang="en">
<head>
<meta charset="utf-8">
<title>Ashes Beneath the Orchard</title>
<link href="https://fonts.googleapis.com/css2?family=EB+Garamond:wght@500&family=Oxygen:wght@400;700&family=Open+Sans:wght@300;400&display=swap" rel="stylesheet">
<style>
:root{
  --red:#d4161f;
  --red-dark:#b80f17;
  --red-deep:#8e0a10;
  --navy:#1c1b6b;
  --navy-dark:#0a0a38;
  --navy-light:#4c4aa8;
  --ink:#333;
  --muted:#777;
  --white:#fff;
  --footer:#f2f2f2;
}
*{margin:0;padding:0;box-sizing:border-box}
html,body{width:1176px;height:1200px;overflow:hidden;background:var(--white)}
body{position:relative;font-family:"Open Sans",sans-serif;color:var(--ink)}
.abs{position:absolute}

.site-header{position:absolute;left:0;top:0;width:1176px;height:113px;background:linear-gradient(180deg,#e3252d,var(--red-dark));border-bottom:3px solid #e84a4f}
.brand{left:112px;top:22px;font-family:"EB Garamond",serif;font-weight:500;font-size:29px;line-height:34px;color:var(--white);letter-spacing:.5px}
.nav a{position:absolute;top:52px;font-family:"Oxygen",sans-serif;font-size:18px;color:#f6b3b5;text-decoration:none;white-space:nowrap}
.nav a.active{color:var(--white)}

.hero{position:absolute;left:0;top:113px;width:1176px;height:475px;background:linear-gradient(90deg,var(--navy-dark) 0%,#1d1c6e 45%,#2a2880 70%,var(--navy-light) 100%)}
.hero-title{left:113px;top:120px;font-family:"Oxygen",sans-serif;font-weight:700;font-size:46px;line-height:50px;color:var(--white);white-space:nowrap}
.hero-sub{left:113px;top:170px;font-family:"Oxygen",sans-serif;font-size:35px;line-height:40px;color:var(--white);white-space:nowrap}
.hero-text{left:118px;top:215px;width:400px;font-weight:300;font-size:13px;line-height:23px;color:#c9c9ee}
.hero-price{left:120px;top:262px;font-family:"Oxygen",sans-serif;font-size:36px;line-height:40px;color:var(--white)}
.btn{position:absolute;display:flex;align-items:center;justify-content:center;font-family:"Open Sans",sans-serif;font-size:13px;color:var(--white);text-decoration:none;border-radius:2px;white-space:nowrap}
.btn-navy{background:linear-gradient(180deg,#2d2c8e,var(--navy));box-shadow:0 1px 2px rgba(0,0,0,.3)}
.btn-hero{left:117px;top:320px;width:131px;height:38px;background:linear-gradient(180deg,#3735a8,#24238a)}
.book-art{left:660px;top:50px;width:363px;height:367px;background:linear-gradient(135deg,#7a1a22 0%,#a8323a 30%,#2d2a86 55%,#c5b8b0 80%,#6b1218 100%);border-radius:3px}
.dots{left:557px;top:447px;display:flex;gap:4px}
.dots span{width:12px;height:12px;border-radius:50%;background:#8e8cc9}
.dots span.on{background:var(--white)}

.features{position:absolute;left:0;top:588px;width:1176px;height:210px}
.card{position:absolute;top:0;height:210px;border:1px solid #e2e2e2;background:linear-gradient(180deg,#fff 70%,#f5f5f5)}
.card h2{position:absolute;font-family:"Oxygen",sans-serif;font-weight:400;font-size:24px;line-height:30px;color:var(--navy);white-space:nowrap}
.card p{position:absolute;width:260px;font-size:12.5px;line-height:21px;color:var(--muted)}
.card .btn{width:103px;height:33px}
.card.response h2{color:var(--red)}
.btn-red{background:linear-gradient(180deg,#e8262e,var(--red-dark))}

.about-title{left:110px;top:848px;font-family:"Oxygen",sans-serif;font-size:28px;line-height:34px;color:#333}
.about-text{left:110px;width:640px;font-size:12.5px;line-height:22.3px;color:var(--muted)}
.order{left:777px;top:841px;width:277px;height:193px;border-radius:3px;background:linear-gradient(120deg,#cf1820 0%,#cf1820 32%,#e0262d 33%,#d71d25 100%);overflow:hidden}
.order h2{position:absolute;left:33px;top:28px;font-family:"Oxygen",sans-serif;font-weight:400;font-size:28px;line-height:32px;color:var(--white)}
.order p{position:absolute;left:33px;top:61px;width:220px;font-size:12.5px;line-height:20.5px;color:#fde4e5}
.btn-dark{left:33px;top:136px;width:136px;height:33px;background:linear-gradient(180deg,#7a0a0e,#5c0609)}

.site-footer{position:absolute;left:0;top:1090px;width:1176px;height:110px;background:var(--footer);border-top:1px solid #ddd}
.foot-nav{left:118px;top:25px;font-family:"Oxygen",sans-serif;font-size:15px;color:#444;white-space:nowrap}
.foot-nav a{color:#444;text-decoration:none}
.foot-nav .sep{margin:0 7px}
.copy{left:118px;top:59px;font-size:12.5px;color:#777}
.foot-brand{left:745px;top:21px;width:56px;height:56px;border-radius:50%;background:#111;display:flex;align-items:center;justify-content:center;font-family:"Oxygen",sans-serif;font-weight:700;font-size:15px;color:var(--white)}
.social{left:944px;top:33px;display:flex;gap:8px}
.social span{width:23px;height:23px;border-radius:2px;background:#3b5fa0}
.social span:nth-child(2){background:#45b0e3}
.social span:nth-child(3){background:#1b74b4}
.social span:nth-child(4){background:#2f7be0}
</style>
</head>
<body>

<header class="site-header">
  <div class="abs brand">ASHES BENEATH<br>THE ORCHARD</div>
  <nav class="nav">
    <a class="active" style="left:426px" href="#">Home</a>
    <a style="left:512px" href="#">About Novel</a>
    <a style="left:651px" href="#">Book Now</a>
    <a style="left:771px" href="#">Blog</a>
    <a style="left:845px" href="#">Testimonial</a>
    <a style="left:978px" href="#">Contact</a>
  </nav>
</header>

<section class="hero">
  <h1 class="abs hero-title">BUY THE LATEST NOVEL</h1>
  <div class="abs hero-sub">Ashes beneath the orchard</div>
  <p class="abs hero-text">Maecenas at justo id velit placerat molestie Donec dictum lectus non odio Cras a ante vitae enim iaculis aliquam</p>
  <div class="abs hero-price">$ 14.99</div>
  <a class="btn btn-hero" href="#">BOOK NOW</a>
  <div class="abs book-art" role="img" aria-label="Front and back covers of the novel Ashes beneath the orchard"></div>
  <div class="abs dots"><span class="on"></span><span></span><span></span><span></span></div>
</section>

<section class="features">
  <div class="card" style="left:0;width:427px">
    <h2 style="left:118px;top:40px">Book Novel Now</h2>
    <p style="left:119px;top:70px">Etiam est nunc venenatis in tristique eu imperdiet ac nisl Cum sociis natoque penati-bus et magnis dis parturient</p>
    <a class="btn btn-navy" style="left:119px;top:143px" href="#">READ MORE</a>
  </div>
  <div class="card" style="left:426px;width:323px">
    <h2 style="left:32px;top:39px">Special About</h2>
    <p style="left:33px;top:69px">Etiam est nunc venenatis in tristique eu imperdiet ac nisl Cum sociis natoque penati-bus et magnis dis parturient</p>
    <a class="btn btn-navy" style="left:33px;top:143px" href="#">READ MORE</a>
  </div>
  <div class="card response" style="left:748px;width:428px">
    <h2 style="left:28px;top:36px">Customer Response</h2>
    <p style="left:29px;top:67px">Etiam est nunc venenatis in tristique eu imperdiet ac nisl Cum sociis natoque penati-bus et magnis dis parturient</p>
    <a class="btn btn-red" style="left:28px;top:143px" href="#">READ MORE</a>
  </div>
</section>

<section class="about">
  <h2 class="abs about-title">Little About My Novel</h2>
  <p class="abs about-text" style="top:890px">Maecenas at justo id velit placerat molestie Donec dictum lectus non odio Cras a ante vitae enim iaculis aliquam Mauris nunc quam venenatis nec euismod sit amet egestas placerat est Pellentesque habitant morbi tristique senectus et netus et malesuada fames ac turpis egestas Cras id elit Integer quis urna Ut ante enim dapibus malesuada fringilla eu condimentum quis tellus Aenean porttitor eros vel dolor</p>
  <p class="abs about-text" style="top:989px">Mauris vel lacus vitae felis vestibulum volutpat Etiam est nunc venenatis in tristique eu imperdiet ac nisl Cum sociis natoque penatibus et magnis dis parturient montes nascetur ridiculus mus In iaculis</p>
  <aside class="abs order">
    <h2>ORDER NOW</h2>
    <p>Morbi tristique senectus et netus et malesuada fames ac turpis egestas Cras id elit Integ</p>
    <a class="btn btn-dark" href="#">CLICK HERE NOW</a>
  </aside>
</section>

<footer class="site-footer">
  <div class="abs foot-nav"><a href="#">Home</a><span class="sep">|</span><a href="#">About Novel</a><span class="sep">|</span><a href="#">Book Now</a><span class="sep">|</span><a href="#">Blog</a><span class="sep">|</span><a href="#">Testimonial</a><span class="sep">|</span><a href="#">Contact</a></div>
  <div class="abs copy">© 2014 Company Name. All right reserved.&nbsp; Term of Use</div>
  <div class="abs foot-brand">KRV</div>
  <div class="abs social" aria-label="Social links"><span></span><span></span><span></span><span></span></div>
</footer>

</body>
</html>
```